Design a leading edge business card for an architectural company

We believe that Velistra Design Collective is redefining the architectural industry. With that, we need a leading edge business card for the company that focuses on landscape architecture, design, and construction.

Our clients are businesses and homeowners so we need a clean, simple, and professional-looking logo. But we want something special. Design must be elegant but unexpected.

Color preferences:
- Preferably with black background but not a must
- Text should be light colored
- Overall, don’t use too much colors.

Content:
- Front of card must contain either just the logo or the logo and business name only.
- Back of card will show the other information (name, title, phone number, email, website, location).

Style:
- Maybe embossing, de-bossing, or spot UV
- Layout should be landscape unless you prove us otherwise.

Size: 1050 x 600 pixels (with 1/8th inch bleed: 1125 x 675 pixels)

Attached is the company logo to incorporate in the design.

```html
<!DOCTYPE html>
<html lang="en">
<head>
<meta charset="utf-8">
<title>Velistra Design Collective — Business Card</title>
<link href="https://fonts.googleapis.com/css2?family=Lato:ital,wght@0,400;0,700;1,400&display=swap" rel="stylesheet">
<style>
  :root {
    --stage: #000000;
    --card: #262626;
    --card-edge: #1c1c1c;
    --ink: #f2f2f2;
    --ink-soft: #c9c9c9;
    --ink-muted: #9a9a9a;
  }
  * { margin: 0; padding: 0; box-sizing: border-box; }
  html, body {
    width: 1200px; height: 675px; overflow: hidden;
    background: var(--stage);
    font-family: "Lato", Arial, sans-serif;
    color: var(--ink);
  }
  .stage {
    position: relative; width: 1200px; height: 675px;
    display: flex; align-items: center; justify-content: center; gap: 50px;
  }
  .card {
    position: relative; width: 525px; height: 300px;
    background: var(--card);
    box-shadow: 0 0 0 1px var(--card-edge);
  }
  .wordmark {
    font-family: "Lato", Arial, sans-serif;
    font-weight: 400;
    text-transform: uppercase;
    color: var(--ink);
    text-align: center;
    letter-spacing: 0.08em;
    line-height: 1.15;
  }

  /* Information side */
  .card--info .holder {
    position: absolute; left: 196px; top: 26px;
  }
  .holder__name { font-size: 13px; font-weight: 700; color: var(--ink); }
  .holder__title { font-size: 8.5px; font-style: italic; color: var(--ink-muted); margin-top: 3px; }
  .card--info .wordmark {
    position: absolute; left: 28px; top: 96px; width: 160px;
    font-size: 17px;
  }
  .contact {
    position: absolute; left: 196px; top: 178px;
    list-style: none; font-size: 10px; color: var(--ink-soft);
  }
  .contact__address { line-height: 1.45; margin-bottom: 4px; }
  .contact li { display: flex; align-items: center; gap: 6px; line-height: 1.5; }
  .contact svg { width: 9px; height: 9px; fill: var(--ink-soft); flex: none; }

  /* Logo side */
  .card--brand .wordmark {
    position: absolute; left: 0; right: 0; top: 116px;
    font-size: 26px;
  }
  .card--brand .site {
    position: absolute; left: 0; right: 0; top: 238px;
    text-align: center; font-size: 10px; color: var(--ink-soft);
  }
</style>
</head>
<body>
<main class="stage">
  <section class="card card--info" aria-label="Card back with contact details">
    <div class="holder">
      <p class="holder__name">Mara Elston</p>
      <p class="holder__title">Managing Director</p>
    </div>
    <p class="wordmark">Velistra<br>Design Collective</p>
    <ul class="contact">
      <li class="contact__address">Unit 7, Harbor Lane<br>Lakeview, 4821, Norland</li>
      <li><svg viewBox="0 0 10 10"><path d="M2 0.5 L3.8 2.6 L2.8 3.8 Q4 6.2 6.2 7.2 L7.4 6.2 L9.5 8 L8.2 9.5 Q2.8 9 0.5 1.8 Z"/></svg>(555) 214-3307</li>
      <li><svg viewBox="0 0 10 10"><rect x="2.5" y="0.5" width="5" height="3"/><rect x="0.5" y="3.5" width="9" height="4" rx="0.8"/><rect x="2.5" y="6.5" width="5" height="3"/></svg>(555) 214-3390</li>
      <li><svg viewBox="0 0 10 10"><path d="M0.5 2 H9.5 V8.5 H0.5 Z M1.3 2.6 L5 5.6 L8.7 2.6" fill="none" stroke="#c9c9c9" stroke-width="0.9"/></svg>info@velistradesign.com</li>
      <li><svg viewBox="0 0 10 10"><circle cx="5" cy="5" r="4.3" fill="none" stroke="#c9c9c9" stroke-width="0.9"/><path d="M0.7 5 H9.3 M5 0.7 Q2.2 5 5 9.3 M5 0.7 Q7.8 5 5 9.3" fill="none" stroke="#c9c9c9" stroke-width="0.7"/></svg>www.velistradesign.com</li>
    </ul>
  </section>

  <section class="card card--brand" aria-label="Card front with company name">
    <p class="wordmark">Velistra<br>Design Collective</p>
    <p class="site">www.velistradesign.com</p>
  </section>
</main>
</body>
</html>
```